Business Card Design

as above
one side to be name of business and information about business inside an imessage text bubble.
other side to be contact details around an email icon . 'envelope'

Target Market(s)

seniors

Industry/Entity Type

Business

Contact Information for Business Card

Tech Along-Keep Along
Marlene Hobb
0461 837 204
Marlene.techalong@quillmail.test
ABN:74618250913

Technology help for seniors in your own home.- tablets, music players, mobile phones, internet, email, computers. No question too small.

```html
<!DOCTYPE html>
<html lang="en">
<head>
<meta charset="utf-8">
<title>Tech Along-Keep Along — Business Card</title>
<link rel="stylesheet" href="https://fonts.googleapis.com/css2?family=Cabin:wght@400;700&display=swap">
<style>
  :root {
    --bubble: #f0aa58;
    --name-ink: #7a1200;
    --ink: #1c1c1c;
    --paper: #ffffff;
  }
  html, body {
    margin: 0;
    padding: 0;
    width: 1200px;
    height: 741px;
    overflow: hidden;
    background: var(--paper);
  }
  .card {
    position: relative;
    width: 1200px;
    height: 741px;
    overflow: hidden;
    background: var(--paper);
  }
  .speech-bubble {
    position: absolute;
    inset: 0;
    width: 1200px;
    height: 741px;
  }
  .speech-bubble path,
  .speech-bubble ellipse { fill: var(--bubble); }

  .business-name {
    position: absolute;
    left: 0;
    top: 100px;
    width: 1200px;
    margin: 0;
    font-family: "Cabin", sans-serif;
    font-weight: 700;
    font-size: 86px;
    line-height: 92px;
    color: var(--name-ink);
  }
  .business-name .line { display: block; }
  .business-name .line-one { padding-left: 278px; }
  .business-name .line-two { padding-left: 348px; }

  .service-summary {
    position: absolute;
    left: 0;
    top: 334px;
    width: 1216px;
    margin: 0;
    text-align: center;
    font-family: "Cabin", sans-serif;
    font-weight: 400;
    font-size: 42px;
    line-height: 45px;
    color: var(--ink);
  }
  .tagline {
    position: absolute;
    left: 0;
    top: 474px;
    width: 1216px;
    margin: 0;
    text-align: center;
    font-family: "Cabin", sans-serif;
    font-weight: 700;
    font-size: 48px;
    line-height: 56px;
    color: var(--ink);
  }
</style>
</head>
<body>
  <main class="card">
    <svg class="speech-bubble" viewBox="0 0 1200 741" aria-hidden="true">
      <ellipse cx="603" cy="320" rx="532" ry="281"/>
      <path d="M470 560 C 490 625, 450 680, 378 702 C 500 690, 600 640, 660 575 Z"/>
    </svg>

    <h1 class="business-name">
      <span class="line line-one">Tech Along-</span>
      <span class="line line-two">Keep Along</span>
    </h1>

    <p class="service-summary">
      Technology help for seniors in your own home.-<br>
      tablets, music players, mobile phones, internet,<br>
      email, computers.
    </p>

    <p class="tagline">No question too small.</p>
  </main>
</body>
</html>
```